Creation of foldable A4 Leaflet to summarise my website

I need to summarize the content of my website into a 4 facecs-2 pages A4 foldable leaflet. I need the leaflet to go through the main topics of my website, with accurate descriptions and some pics taken from the website. Focusing about professionality and over 25 year experience on the field. Give also apace to our valued partners and customers
My website plimborex.au

Target Market(s)

Industrial filtration, dust collector business

Industry/Entity Type

Industrial filtration, dust collectors market, mining, powerplant, cement industry

Font styles to use
Sans Serif

Colors
0054AA
0677BA
7BADD7
CADEEF
E8F1F8

Requirements
Must have
• clear references to my website
Nice to have
• clear and clean layout
Should not have
• dark colours other than blue and navy, as per my logo

```html
<!DOCTYPE html>
<html lang="en">
<head>
<meta charset="utf-8">
<title>Plimborex Environmental Services – Leaflet</title>
<link href="https://fonts.googleapis.com/css2?family=Poppins:wght@400;500;600;700;800&display=swap" rel="stylesheet">
<style>
:root{
  --blue-deep:#0054AA;
  --blue-mid:#0677BA;
  --blue-soft:#7BADD7;
  --blue-pale:#CADEEF;
  --blue-mist:#E8F1F8;
  --royal:#1f5fd0;
  --navy:#13284a;
  --ink:#3a3f47;
  --slate:#6f86a6;
  --page:#ffffff;
  --bg:#f2f4f7;
}
*{margin:0;padding:0;box-sizing:border-box}
html,body{width:1200px;height:1199px;overflow:hidden}
body{background:var(--bg);font-family:'Poppins',sans-serif;color:var(--ink);position:relative}
.page{position:absolute;background:var(--page);box-shadow:0 4px 14px rgba(20,40,80,.12);overflow:hidden}
.abs{position:absolute}
.body-text{font-size:6.4px;line-height:1.32;text-align:justify;color:#444}
.brand{display:flex;align-items:center;gap:7px}
.brand-dot{width:26px;height:26px;border-radius:50%;flex:none}
.brand-name{font-weight:700;letter-spacing:1px;line-height:1.1}

/* cover */
.cover{left:250px;top:78px;width:345px;height:503px}
.cover .brand{left:24px;top:288px}
.cover .brand-dot{background:var(--blue-mid)}
.cover .brand-name{font-size:11px;color:var(--navy)}
.cover-kicker{left:24px;top:350px;font-size:10.5px;color:var(--blue-mid)}
.cover-title{left:24px;top:364px;width:300px;font-size:17.5px;font-weight:700;line-height:1.28;color:var(--navy)}
.cover-rule{left:24px;top:431px;width:290px;height:1px;background:var(--navy)}
.cover-lead{left:24px;top:437px;width:295px;font-size:6.2px;line-height:1.3;color:#333}
.pill{left:24px;top:467px;padding:2px 6px;border-radius:6px;background:var(--navy);color:#fff;font-size:6.4px}

/* back */
.back{left:604px;top:75px;width:346px;height:505px;background:linear-gradient(160deg,#2363d6 0%,#1d5bcc 55%,#1a4fb4 100%)}
.back .brand{left:86px;top:90px}
.back .brand-dot{background:#fff;width:34px;height:34px}
.back .brand-name{font-size:14px;color:#fff}
.contact-kicker{left:0;top:195px;width:346px;text-align:center;font-size:15px;color:#fff}
.contact-title{left:0;top:215px;width:346px;text-align:center;font-size:30px;font-weight:700;color:#fff}
.contact-lead{left:30px;top:280px;width:286px;text-align:center;font-size:9.2px;line-height:1.4;color:#fff;font-weight:500}
.back-band{left:0;top:418px;width:346px;height:87px;background:linear-gradient(90deg,#123a78,#0f2a52)}
.phone{left:40px;top:444px;display:flex;align-items:center;gap:5px;color:#fff;font-size:16px;font-weight:600}
.contact-list{left:212px;top:432px;color:#fff;font-size:7.2px;line-height:1}
.contact-list li{list-style:none;display:flex;align-items:center;gap:4px;margin-bottom:5px}
.contact-list li.gap{margin-top:9px}
.contact-list svg{flex:none}

/* spread */
.spread{left:250px;top:612px;width:700px;height:512px}
.half{position:absolute;top:0;width:350px;height:512px}
.half.left{left:0}
.half.right{left:350px}
.spine{left:349px;top:0;width:2px;height:512px;background:linear-gradient(90deg,rgba(0,0,0,.06),rgba(0,0,0,0))}

.h-big{font-size:27px;font-weight:700;line-height:1}
.h-grey{color:#4a4e55}
.h-blue{color:var(--blue-soft)}
.services-sub{left:30px;top:112px;font-size:10px;font-weight:600;line-height:1.3;color:var(--blue-soft)}
.svc-list{left:20px;top:270px;width:119px;height:220px;border-radius:8px;background:linear-gradient(180deg,#6f8db1,#8197b3);padding:9px 8px;color:#fff}
.svc-list h3{font-size:11px;font-weight:700;margin-bottom:4px}
.svc-list li{font-size:6.2px;line-height:1.25;margin:0 0 5px 10px;padding-left:0}
.card{width:96px;height:116px;border-radius:8px;background:linear-gradient(180deg,#7ab0e3,#5f9ad6);color:#fff;padding:9px 8px}
.card h4{font-size:6.8px;font-weight:700;line-height:1.2;margin-bottom:7px}
.card p{font-size:5.9px;line-height:1.25}

.about-sub{left:18px;top:130px;font-size:17px;font-weight:700;line-height:1.35;color:var(--blue-soft)}
.why{left:18px;top:340px;width:305px;height:146px;border-radius:10px;background:linear-gradient(135deg,#3c526f,#1c3050);overflow:hidden}
.why-kicker{left:14px;top:12px;font-size:12px;color:#fff}
.why-title{left:14px;top:24px;font-size:19px;font-weight:700;color:var(--blue-pale)}
.why-title span{font-size:11px;font-weight:400;color:#fff}
.why-text{left:14px;top:60px;width:116px;font-size:6.3px;line-height:1.3;font-weight:600;color:#fff;text-align:justify}
.clients{left:137px;top:7px;width:160px;height:132px;border-radius:8px;background:#fff;padding:8px}
.clients h3{font-size:13px;font-weight:700;color:var(--navy);text-align:center;margin-bottom:6px}
.client-grid{display:grid;grid-template-columns:repeat(4,1fr);gap:6px 3px}
.client{font-size:5.4px;font-weight:700;color:var(--navy);display:flex;align-items:center;gap:2px;height:13px}
.client i{width:4px;height:4px;background:var(--blue-mid);flex:none}
</style>
</head>
<body>

<!-- Front cover -->
<section class="page cover">
  <svg class="abs" style="left:0;top:0" width="345" height="300" viewBox="0 0 345 300">
    <defs>
      <linearGradient id="coverSwoosh" x1="0" y1="1" x2="1" y2="0">
        <stop offset="0" stop-color="#2b74d6"/><stop offset="1" stop-color="#6fb4e6"/>
      </linearGradient>
      <linearGradient id="coverPhoto" x1="0" y1="0" x2="1" y2="1">
        <stop offset="0" stop-color="#e9dcc0"/><stop offset=".5" stop-color="#f3efe8"/><stop offset="1" stop-color="#d8b878"/>
      </linearGradient>
    </defs>
    <circle cx="150" cy="88" r="190" fill="url(#coverSwoosh)"/>
    <circle cx="118" cy="60" r="180" fill="#fff"/>
    <path d="M0 0 H250 A150 150 0 0 1 0 205 Z" fill="url(#coverPhoto)" role="img" aria-label="Photo of new filter bags and cartridges in white, tan and gold fabrics"/>
  </svg>
  <div class="abs brand"><span class="brand-dot"></span><span class="brand-name">PLIMBOREX<br>ENVIRONMENTAL SERVICES</span></div>
  <div class="abs cover-kicker">Plimborex Environmental Services</div>
  <h1 class="abs cover-title">PREMIUM DUST COLLECTOR SUPPLY &amp; EXPERT MAINTENANCE SOLUTIONS</h1>
  <div class="abs cover-rule"></div>
  <p class="abs cover-lead">We provide accredited dust collection systems and comprehensive servicing to ensure industrial facilities maintain peak operational performance and environmental compliance.</p>
  <div class="abs pill">www.plimborex.au</div>
</section>

<!-- Back cover -->
<section class="page back">
  <div class="abs brand"><span class="brand-dot"></span><span class="brand-name">PLIMBOREX<br>ENVIRONMENTAL SERVICES</span></div>
  <div class="abs contact-kicker">CONTACT US</div>
  <h2 class="abs contact-title">GET IN TOUCH</h2>
  <p class="abs contact-lead">Fill in your details below and we’ll get back to you as soon as possible or call us directly:</p>
  <div class="abs back-band"></div>
  <div class="abs phone">
    <svg width="9" height="14" viewBox="0 0 9 14"><path d="M7 1 C2 2 1 5 1 7 C1 9 2 12 7 13 L8 10 L6 9 C4.5 9 4 8 4 7 C4 6 4.5 5 6 5 L8 4 Z" fill="#fff"/></svg>
    0400 555 218
  </div>
  <ul class="abs contact-list">
    <li><svg width="7" height="6" viewBox="0 0 7 6"><rect x=".5" y=".5" width="6" height="5" fill="none" stroke="#fff"/><path d="M.5 .5 L3.5 3 L6.5 .5" fill="none" stroke="#fff"/></svg>hello@plimborex.au</li>
    <li><svg width="7" height="7" viewBox="0 0 7 7"><circle cx="3.5" cy="3.5" r="3" fill="none" stroke="#fff" stroke-width=".8"/><path d="M.5 3.5 H6.5 M3.5 .5 V6.5" stroke="#fff" stroke-width=".6"/></svg>www.plimborex.au</li>
    <li class="gap"><svg width="6" height="6" viewBox="0 0 6 6"><circle cx="3" cy="3" r="2.6" fill="#fff"/></svg>plimborex_env</li>
  </ul>
</section>

<!-- Inside spread -->
<section class="page spread">
  <div class="half left">
    <svg class="abs" style="left:0;top:0" width="350" height="200" viewBox="0 0 350 200">
      <defs>
        <linearGradient id="svcSwoosh" x1="0" y1="0" x2="1" y2="1">
          <stop offset="0" stop-color="#6fb4e6"/><stop offset="1" stop-color="#2b6fd2"/>
        </linearGradient>
      </defs>
      <path d="M210 0 C175 60 205 160 350 155 L350 135 C260 140 220 80 245 0 Z" fill="url(#svcSwoosh)"/>
      <path d="M252 0 H350 V128 A80 80 0 0 1 252 0 Z" fill="#8a8f96" role="img" aria-label="Photo of technicians in protective suits servicing filter bags inside a dust collector"/>
    </svg>
    <div class="abs h-big h-grey" style="left:30px;top:46px">OUR</div>
    <div class="abs h-big h-blue" style="left:30px;top:80px">SERVICES</div>
    <div class="abs services-sub">INDUSTRIAL DUST<br>COLLECTOR SUPPLY &amp; EXPERT<br>MAINTENANCE RELIABILITY</div>
    <p class="abs body-text" style="left:30px;top:156px;width:230px">Delivering advanced environmental solutions is at the core of what this business achieves for the industrial sector. We specialise in the supply and rigorous servicing of high-performance dust collectors designed to withstand the demanding conditions of Australia wide industrial sites. Our team focuses on ensuring your facility meets all necessary air quality standards through precise engineering and dedicated support.</p>
    <p class="abs body-text" style="left:30px;top:220px;width:298px">Maximising the lifespan of your equipment requires a partner who understands the intricacies of filtration technology. We offer a complete suite of services from initial supply to extraordinary maintenance, ensuring that every component functions at its absolute best. By choosing an accredited provider, you gain the assurance of technical excellence and a commitment to maintaining a clean, safe, and efficient workspace.</p>

    <div class="abs svc-list">
      <h3>OUR SERVICES</h3>
      <ul>
        <li>Dust Collectors Servicing</li>
        <li>Dust Collectors Supply</li>
        <li>Dust Collectors Spare Parts Supply</li>
        <li>Filtration Bags Install</li>
        <li>Filtration Bags Supply</li>
        <li>Site Supervision &amp; Project Management</li>
        <li>Dust Collectors Regular Maintenance</li>
        <li>Dust Collectors Extraordinary Maintenance</li>
        <li>Dust Collector Inspection to Meet EPA Standards</li>
        <li>Leak Test</li>
        <li>Laboratory Analysis of Sample Bags</li>
      </ul>
    </div>
    <div class="abs card" style="left:146px;top:277px"><h4>DUST COLLECTORS SERVICING</h4><p>We conduct thorough technical assessments and mechanical repairs to ensure your dust collection systems operate with maximum efficiency and reliability across all industrial applications.</p></div>
    <div class="abs card" style="left:246px;top:277px;width:92px"><h4>DUST COLLECTORS SUPPLY</h4><p>Our team provides high-capacity, accredited dust collection units tailored to the specific volume and material requirements of your facility for optimal air filtration.</p></div>
    <div class="abs card" style="left:146px;top:398px;height:98px"><h4>DUST COLLECTORS SPARE PARTS SUPPLY</h4><p>We stock and distribute essential components and high-quality spare parts to minimise downtime and keep your environmental systems running without interruption.</p></div>
    <div class="abs card" style="left:246px;top:398px;width:92px;height:103px"><h4>DUST COLLECTORS SERVICING</h4><p>We conduct thorough technical assessments and mechanical repairs to ensure your dust collection systems operate with maximum efficiency and reliability across all industrial applications.</p></div>
  </div>

  <div class="half right">
    <svg class="abs" style="left:0;top:0" width="350" height="200" viewBox="0 0 350 200">
      <defs>
        <linearGradient id="aboutSwoosh" x1="0" y1="0" x2="1" y2="1">
          <stop offset="0" stop-color="#2f7ad8"/><stop offset="1" stop-color="#2060cc"/>
        </linearGradient>
      </defs>
      <path d="M185 0 C160 70 200 180 350 178 L350 158 C270 158 215 95 220 0 Z" fill="url(#aboutSwoosh)"/>
      <path d="M224 0 H342 V118 A62 70 0 0 1 224 0 Z" fill="#7d7a72" role="img" aria-label="Photo of the interior of a dust collector housing with rows of filter bags"/>
    </svg>
    <div class="abs h-big" style="left:18px;top:80px"><span class="h-grey">ABOUT</span> <span style="color:var(--blue-deep)">US</span></div>
    <div class="abs about-sub">THE JOURNEY OF<br>ENVIRONMENTAL<br>SERVICE EXCELLENCE</div>
    <p class="abs body-text" style="left:18px;top:216px;width:304px">Originating from a desire to provide more robust technical support to the Australia wide industrial sector, we began our journey by focusing on the critical need for reliable dust management. We recognised that many facilities struggled with maintaining complex filtration systems, and we stepped in to offer a more dedicated, hands-on approach. This foundation allowed us to build a reputation based on technical merit and unwavering support for our clients.</p>
    <p class="abs body-text" style="left:18px;top:275px;width:304px">Growing with the industries we serve, we have refined our processes to address the unique challenges of sectors like cement manufacturing, grain handling, lithium processing and power generation. We choose to aim for excellence because we understand that our work is vital to the operational continuity of our partners. Our history is one of continuous learning and adaptation, ensuring we remain at the forefront of environmental servicing and supply.</p>

    <div class="abs why">
      <div class="abs why-kicker">WHY</div>
      <div class="abs why-title">CHOOSE <span>US?</span></div>
      <p class="abs why-text">We bring over two decades of technical proficiency to every project, ensuring your systems are maintained by an accredited team.<br><br>Our focus remains on delivering reliable outcomes that keep your operations compliant and efficient.</p>
      <div class="abs clients">
        <h3>OUR CLIENTS</h3>
        <div class="client-grid">
          <span class="client"><i></i>Westmark</span>
          <span class="client">Corvane</span>
          <span class="client">Redgum Brick</span>
          <span class="client"><i></i>Stonevale</span>
          <span class="client">Airlith</span>
          <span class="client">Feltwise</span>
          <span class="client">Ashgrove</span>
          <span class="client">Harbour Concrete</span>
          <span class="client">Goldfield Grains</span>
          <span class="client">Corvane</span>
          <span class="client">Southbay Cement</span>
          <span class="client">Calder Cement</span>
          <span class="client"><i></i>Limeport</span>
          <span class="client">Civiltek</span>
          <span class="client">Quarrix</span>
          <span class="client">Dunmore</span>
        </div>
      </div>
    </div>
  </div>
  <div class="abs spine"></div>
</section>

</body>
</html>
```